Bayside Critter Welcome MEET

Hi ALL!
We need an 8.5 X 11 inch, one page flyer to include all the below copy plus 8 sponsoring logos at the very bottom.
Thank YOU!

Birch Hollow Critter MEET
(Fun for Animals In Rescue!)

Sunday, August 12, 2018
1 to 4:30 p.m.

Animal Education & Adoption Event
featuring:

Harbor Pet Shelter & Services Rabbits & Mice

Meadow Browsers Goats

Kindly Hounds Haven

Featherwing Pigeons & Doves

Comet Pup Haven

Marge’s Feline Haven

Marvel Mutt Haven

Special Guest from 1-3 p.m.
BeBop - SF's 1st Therapy Pig!
Instagram: @BEBOP_BAYHOG
Facebook: @BEBOP THE HOG

Activities for Kids
Dog & Cat Toy Making with Greta Holloway Canine School
Animal Mask Making with Tiny Crafters
Face-in-a-Hole Photo Fun with Mark Dorsey Canine School

HPSS FREE Giveaway!
First 75 attending families receive a FREE PSS Doggie Bag containing a dog water bottle, food, shampoo, toy, treats and blinking dog collar light.

Animal Tails

1 pm Winnie’s Nook Storytime

1:30 p.m. BeBop the Therapy Pig

1:45 pm “Twig the Shelter Hog”
Read by Author Marian Thistle

2 p.m. Winnie’s Nook Singalong

2:30 p.m. Featherwing Bird Haven

2:45 p.m. Quire Pages Storytime

3 pm Meadow Browsers Refuge

3:15 p.m. The Hedge Burrow Puppet Show

3:45 pm HPSS Officer Norma

4 p.m. Winnie’s Nook Storytime

Font styles to use
Serif

Colors

Designer to choose colors to be used in the design.

Requirements
Must have
• pig, goat, 2 dogs, kitten, dove, bunny

```html
<!DOCTYPE html>
<html lang="en">
<head>
<meta charset="utf-8">
<title>Birch Hollow Critter MEET</title>
<link href="https://fonts.googleapis.com/css2?family=Crimson+Pro:ital,wght@0,400;0,600;0,700;1,400;1,600;1,700&display=swap" rel="stylesheet">
<style>
:root{
  --backdrop:#8f8f8f;
  --paper-light:#f4f4f4;
  --paper-mid:#d6d6d6;
  --paper-dark:#c2c2c2;
  --lime:#b2d235;
  --sky:#27a8e0;
  --magenta:#e5007e;
  --sun:#ffdd19;
  --ink:#1c1c1c;
  --white:#ffffff;
}
*{margin:0;padding:0;box-sizing:border-box}
html,body{width:1200px;height:1200px;overflow:hidden;background:var(--backdrop)}
body{font-family:"Crimson Pro",Georgia,serif;color:var(--ink)}
.flyer{position:absolute;left:180px;top:57px;width:840px;height:1086px;overflow:hidden;
  background:radial-gradient(ellipse at 45% 55%,var(--paper-light) 0%,var(--paper-mid) 45%,var(--paper-light) 70%,var(--paper-dark) 100%)}
.top-strip{position:absolute;left:0;top:0;width:840px;height:23px;background:#e6e6e6}
.photo{position:absolute}
.photo-pigs{left:0;top:23px;width:267px;height:228px;background:linear-gradient(135deg,#6b3b26,#e9b3b0 55%,#b88a5a)}
.photo-goats{left:281px;top:23px;width:278px;height:228px;background:linear-gradient(135deg,#4a2f22,#7d5a45 50%,#c8b4a0)}
.photo-puppies{left:573px;top:23px;width:267px;height:228px;background:linear-gradient(135deg,#3a2a1f,#b98448 50%,#2b2320)}
.photo-doves{left:0;top:798px;width:152px;height:160px;background:linear-gradient(160deg,#2d5a2a,#dfe3e6 55%,#6f6a5e)}
.photo-bunnies{left:161px;top:798px;width:163px;height:160px;background:linear-gradient(135deg,#b6a58a,#a0713e 55%,#d5c3a0)}
.photo-kittens{left:333px;top:798px;width:164px;height:160px;background:linear-gradient(135deg,#4a3b33,#e8e4df 50%,#4f7a32)}
.date-tab{position:absolute;left:242px;top:0;width:356px;height:84px;background:var(--lime);border-radius:0 0 12px 12px;
  text-align:center;font-style:italic;font-weight:600;font-size:26px;line-height:32px;padding-top:10px}
.title-band{position:absolute;left:0;top:251px;width:840px;height:110px;background:var(--sky);text-align:center}
.title-band h1{font-weight:700;font-size:62px;line-height:110px;color:var(--white);letter-spacing:0.5px;
  text-shadow:2px 2px 3px rgba(0,0,0,.55)}
.tagline{position:absolute;left:215px;top:361px;width:399px;height:53px;background:var(--magenta);border-radius:0 0 12px 12px;
  color:var(--white);font-style:italic;font-size:27px;text-align:center;line-height:50px}
.col{position:absolute}
.col-left{left:84px;top:436px;width:375px}
.col-right{left:537px;top:436px;width:290px}
h2{font-weight:600;font-size:20px;line-height:25px;margin-bottom:3px}
ul{list-style:none}
li{font-size:14.5px;line-height:25px}
li::before{content:"• "}
.section{margin-bottom:15px}
.giveaway p{font-size:14.5px;line-height:18px;margin-top:2px}
.sponsors-label{position:absolute;left:84px;top:972px;font-style:italic;font-weight:600;font-size:13px}
.sponsor{position:absolute;width:91px;height:35px;background:var(--white);border:1px solid #6a6a6a}
.schedule{position:absolute;left:522px;top:700px;width:296px;height:362px;background:var(--sun);border-radius:12px;
  box-shadow:0 3px 6px rgba(0,0,0,.3)}
.schedule-head{position:absolute;left:0;top:22px;width:296px;height:48px;background:#1d1b1b}
.schedule-head h3{position:absolute;left:98px;top:2px;color:var(--white);font-style:italic;font-weight:700;font-size:32px;line-height:44px;white-space:nowrap}
.book-art{position:absolute;left:4px;top:-20px;width:84px;height:82px;background:linear-gradient(160deg,#fbf7ee,#d6c9ad 70%,#8a6a3e);border-radius:4px}
.schedule-list{position:absolute;left:16px;top:83px;list-style:none}
.schedule-list li{font-size:14.5px;line-height:25px;display:flex;white-space:nowrap}
.schedule-list li::before{content:none}
.schedule-list .time{font-weight:700;width:65px;flex:none}
.schedule-list .note{padding-left:69px}
</style>
</head>
<body>
<main class="flyer">
  <div class="top-strip"></div>
  <div class="photo photo-pigs" role="img" aria-label="Photo of two pink piglets peeking over a wooden fence"></div>
  <div class="photo photo-goats" role="img" aria-label="Photo of two goats looking out of a barn stall"></div>
  <div class="photo photo-puppies" role="img" aria-label="Photo of three puppies at a barn door"></div>

  <div class="date-tab">Sunday, August 12, 2018<br>1:00 - 4:30 p.m.</div>

  <header class="title-band"><h1>Birch Hollow Critter MEET</h1></header>
  <div class="tagline">(Fun for Animals In Rescue!)</div>

  <section class="col col-left">
    <div class="section">
      <h2>Activities for Kids</h2>
      <ul>
        <li>Dog &amp; Cat Toy Making with Greta Holloway Canine School</li>
        <li>Animal Mask Making with Tiny Crafters</li>
        <li>Face-in-a-Hole Photo Fun with Mark Dorsey Canine School</li>
      </ul>
    </div>
    <div class="section giveaway">
      <h2>HPSS FREE Giveaway!</h2>
      <p>First 75 attending families receive a FREE PSS Doggie Bag containing a dog water bottle, food, shampoo, toy, treats and blinking dog collar light.</p>
    </div>
    <div class="section">
      <h2>Special Guest from 1:00 - 3:00 p.m.</h2>
      <ul>
        <li>BeBop - SF's 1st Therapy Pig!</li>
        <li>Instagram: @BEBOP_BAYHOG</li>
        <li>Facebook: @BEBOP THE HOG</li>
      </ul>
    </div>
  </section>

  <section class="col col-right">
    <h2>Animal Education &amp;<br>Adoption Event featuring:</h2>
    <ul>
      <li>Harbor Pet Shelter &amp; Services Rabbits &amp; Mice</li>
      <li>Meadow Browsers Goats</li>
      <li>Kindly Hounds Haven</li>
      <li>Featherwing Pigeons &amp; Doves</li>
      <li>Comet Pup Haven</li>
      <li>Marge’s Feline Haven</li>
      <li>Marvel Mutt Haven</li>
    </ul>
  </section>

  <div class="photo photo-doves" role="img" aria-label="Photo of two white doves on a fence"></div>
  <div class="photo photo-bunnies" role="img" aria-label="Photo of two brown rabbits resting"></div>
  <div class="photo photo-kittens" role="img" aria-label="Photo of two kittens standing in grass"></div>

  <div class="sponsors-label">SPONSORS:</div>
  <div class="sponsor" style="left:84px;top:993px"></div>
  <div class="sponsor" style="left:189px;top:993px"></div>
  <div class="sponsor" style="left:296px;top:993px"></div>
  <div class="sponsor" style="left:406px;top:993px"></div>
  <div class="sponsor" style="left:84px;top:1036px"></div>
  <div class="sponsor" style="left:189px;top:1036px"></div>
  <div class="sponsor" style="left:296px;top:1036px"></div>
  <div class="sponsor" style="left:406px;top:1036px"></div>

  <aside class="schedule">
    <div class="schedule-head"><h3>Animal Tails</h3></div>
    <div class="book-art" role="img" aria-label="Illustration of an open storybook"></div>
    <ul class="schedule-list">
      <li><span class="time">1:00 p.m.</span>Winnie’s Nook Storytime</li>
      <li><span class="time">1:30 p.m.</span>BeBop the Therapy Pig</li>
      <li><span class="time">1:45 p.m.</span>“Twig the Shelter Hog”</li>
      <li class="note">Read by Author Marian Thistle</li>
      <li><span class="time">2:00 p.m.</span>Winnie’s Nook Singalong</li>
      <li><span class="time">2:30 p.m.</span>Featherwing Bird Haven</li>
      <li><span class="time">2:45 p.m.</span>Quire Pages Storytime</li>
      <li><span class="time">3:00 p.m.</span>Meadow Browsers Refuge</li>
      <li><span class="time">3:15 p.m.</span>The Hedge Burrow Puppet Show</li>
      <li><span class="time">3:45 p.m.</span>HPSS Officer Norma</li>
      <li><span class="time">4:00 p.m.</span>Winnie’s Nook Storytime</li>
    </ul>
  </aside>
</main>
</body>
</html>
```